North Fern Holdings Business Card

A business card design to accompany the logo design you completed on Artisan Hive. We are open to your proposals. I did add one idea below that might work, but we aren't married to the idea. The company is a real estate services company. Clientele are typically high net worth individuals, executive level employment or owners of their own company, 30-60 years old.

Our 1 (bad?) idea: double sided card; One side landscape with logo and word mark. Other side Portrait with the logo only (oversize watermark maybe?). Somewhere add text of Name (Marcus Pellington), Title (Principal), phone # (949-555-0173) and email address (marcus@northfernhq.com). There would be a second design with my wife's name, number and email in place of mine.

Again totally open to ideas here.

Industry/Entity Type

Real Estate

```html
<!DOCTYPE html>
<html lang="en">
<head>
<meta charset="utf-8">
<title>North Fern Holdings Business Card</title>
<link rel="stylesheet" href="https://fonts.googleapis.com/css2?family=Cinzel:wght@400&family=Playfair+Display:ital,wght@1,700&family=Arimo:wght@400&display=swap">
<style>
  :root {
    --sage: #66965a;
    --paper: #ffffff;
    --ink: #111111;
    --canvas: #ffffff;
  }
  * { margin: 0; padding: 0; box-sizing: border-box; }
  html, body {
    width: 1200px; height: 788px; overflow: hidden;
    background: var(--canvas);
  }
  .sheet { position: relative; width: 1200px; height: 788px; }
  .card {
    position: absolute; top: 250px;
    width: 564px; height: 330px;
  }
  .card--front { left: 23px; }
  .card--back { left: 612px; }
  .card__shape { position: absolute; inset: 0; }
  .card__shape .field { fill: var(--sage); }
  .card__shape .panel { fill: var(--paper); }
  .card__shape .seal { fill: var(--paper); }

  .wordmark {
    position: absolute; left: 197px; top: 134px;
    width: 290px; text-align: center;
    font-family: "Cinzel", serif; font-weight: 400;
    color: var(--sage); line-height: 1;
  }
  .wordmark__line { display: block; }
  .wordmark__line--main { font-size: 38px; }
  .wordmark__line--sub { font-size: 30px; letter-spacing: 6px; margin-top: 4px; }

  .holder {
    position: absolute; left: 24px; top: 58px;
    font-family: "Cinzel", serif; color: var(--ink);
  }
  .holder__name { font-size: 24px; letter-spacing: 1.5px; line-height: 1; }
  .holder__name .cap { font-size: 32px; }
  .holder__title {
    font-family: "Playfair Display", serif; font-style: italic; font-weight: 700;
    font-size: 28px; margin: 4px 0 0 78px; line-height: 1;
  }
  .contact {
    position: absolute; left: 22px; top: 196px; width: 330px;
    text-align: center; font-family: "Arimo", sans-serif; color: var(--ink);
  }
  .contact__phone { font-size: 22px; letter-spacing: 0.5px; }
  .contact__email { font-size: 18.5px; margin-top: 10px; letter-spacing: 0.3px; }
</style>
</head>
<body>
<main class="sheet">
  <section class="card card--front" aria-label="Card front">
    <svg class="card__shape" width="564" height="330" viewBox="0 0 564 330">
      <rect class="field" width="564" height="330"/>
      <path class="panel" d="M225 11 H552 V319 H225 A165.4 165.4 0 0 1 225 11 Z"/>
      <circle class="seal" cx="127" cy="170" r="38"/>
    </svg>
    <h1 class="wordmark">
      <span class="wordmark__line wordmark__line--main">North Fern</span>
      <span class="wordmark__line wordmark__line--sub">Holdings</span>
    </h1>
  </section>

  <section class="card card--back" aria-label="Card back">
    <svg class="card__shape" width="564" height="330" viewBox="0 0 564 330">
      <rect class="field" width="564" height="330"/>
      <path class="panel" d="M11 11 H338 A170 170 0 0 1 338 319 H11 Z"/>
      <circle class="seal" cx="432" cy="165" r="40"/>
    </svg>
    <div class="holder">
      <p class="holder__name"><span class="cap">M</span>ARCUS <span class="cap">P</span>ELLINGTON</p>
      <p class="holder__title">Principal</p>
    </div>
    <div class="contact">
      <p class="contact__phone">949-555-0173</p>
      <p class="contact__email">MARCUS@NORTHFERNHQ.COM</p>
    </div>
  </section>
</main>
</body>
</html>
```